Tobias Webpage Design

I would like to start an business and management consultancy business. I am thinking to called it "Krelto Consultancy". Besides the consultancy services, I would also like to provide training on finance, forensic accounting, fraud prevention and internal control.
Professional management consultants are contracted by organizations to provide advisory services in an objective and independent manner.

Services include, but are not limited to, strategic planning, facilitation, quality assurance, education and training, investment counsel, identification and analysis of management problems, developing solutions, and the implementation of proposed solutions.

Professional management consultants are hired when an organization lacks sufficient resources, requires external objective advice, or because they have expertise not available within the client organization.

I would like to see the webpage design that use colors apple green with some other contrast color. The design have to be professional look but with a new age touch.

Reason: Unable to find a suitable web pages design

Dear all

Since last week I post a request, but till to date, I has yet to received a new sparkling creative and "wow" web page design. Please help me here!

Regards

Reason: Yet to found a suitable web designer for my web design. Help! I just need a fresh and professional look design. You may ignore the color code I prefer. Send me your sparkling creative work. Thank you so much!

Some examples

```html
<!DOCTYPE html>
<html lang="en">
<head>
<meta charset="utf-8">
<title>Krelto Consultancy</title>
<link rel="stylesheet" href="https://fonts.googleapis.com/css2?family=PT+Sans:wght@400;700&family=Archivo+Black&display=swap">
<style>
  :root {
    --apple-green: #99cc1a;
    --fold-green: #c4e48a;
    --ink: #000000;
    --paper: #ffffff;
    --panel-grey: #ededed;
    --page-grey: #e3e3e3;
    --footer-text: #d9d9d9;
    --hero-mist: #9aa6b4;
    --hero-deep: #2a3340;
  }
  * { box-sizing: border-box; margin: 0; padding: 0; }
  html, body { width: 1200px; height: 1000px; overflow: hidden; }
  body {
    position: relative;
    background: var(--page-grey);
    font-family: "PT Sans", Tahoma, sans-serif;
    color: var(--ink);
  }
  .site-header {
    position: absolute; top: 0; left: 0; width: 1200px; height: 50px;
    background: var(--paper);
  }
  .brand {
    position: absolute; left: 115px; top: 2px; line-height: 1;
  }
  .brand-name {
    display: block; font-family: "PT Sans", sans-serif; font-weight: 700;
    font-size: 30px; letter-spacing: -0.5px;
  }
  .brand-tag {
    display: block; font-family: "PT Sans", sans-serif; font-weight: 700;
    font-size: 18px; margin-top: -2px;
  }
  .main-nav {
    position: absolute; right: 130px; top: 13px;
    display: flex; gap: 23px; font-size: 15px;
  }
  .main-nav a { color: var(--ink); text-decoration: none; }

  .hero {
    position: absolute; top: 50px; left: 0; width: 1200px; height: 350px;
    background: var(--ink); overflow: hidden;
  }
  .hero-photo {
    position: absolute; left: 360px; top: 0; width: 680px; height: 350px;
    background: radial-gradient(ellipse 50% 75% at 55% 25%, var(--hero-mist) 0%, var(--hero-deep) 55%, var(--ink) 100%);
  }
  .hero-copy {
    position: absolute; left: 128px; top: 58px; color: var(--paper);
  }
  .hero-title {
    color: var(--apple-green); font-size: 37px; font-weight: 400; line-height: 42px;
  }
  .hero-text { font-size: 21px; line-height: 24px; }
  .hero-more { display: block; margin-top: 24px; font-size: 21px; color: var(--paper); text-decoration: none; }

  .content-panel {
    position: absolute; left: 100px; top: 400px; width: 1000px; height: 477px;
    background: var(--panel-grey);
    box-shadow: 0 2px 6px rgba(0,0,0,0.35);
  }
  .content-panel::before {
    content: ""; position: absolute; left: 20px; top: 0; width: 560px; height: 14px;
    background: radial-gradient(ellipse 50% 100% at 50% 0%, rgba(0,0,0,0.35), transparent);
  }
  .story-block {
    position: absolute; left: 122px; top: 103px; font-size: 37px; line-height: 44px; font-weight: 400;
  }
  .plans-card { position: absolute; left: 620px; top: 0; width: 380px; height: 477px; }
  .plans-card svg { position: absolute; inset: 0; }
  .plans-text {
    position: absolute; left: 67px; top: 131px; font-size: 37px; line-height: 44px; font-weight: 400;
  }

  .site-footer {
    position: absolute; left: 0; top: 940px; width: 1200px; height: 60px;
    background: var(--ink); color: var(--footer-text);
  }
  .footer-legal {
    position: absolute; right: 115px; top: 18px; text-align: right;
    font-size: 10px; line-height: 12px; font-family: Tahoma, Verdana, sans-serif;
  }
  .footer-legal .note { margin-right: 145px; }
</style>
</head>
<body>
  <header class="site-header">
    <div class="brand">
      <span class="brand-name">Krelto</span>
      <span class="brand-tag">Consultancy</span>
    </div>
    <nav class="main-nav">
      <a href="#">Home</a>
      <a href="#">About Us</a>
      <a href="#">Services</a>
      <a href="#">Plans</a>
      <a href="#">Contact Us</a>
    </nav>
  </header>

  <section class="hero">
    <div class="hero-photo" role="img" aria-label="Silhouettes of business people, two shaking hands in front of a crowd"></div>
    <div class="hero-copy">
      <h1 class="hero-title">Example Tile</h1>
      <p class="hero-text">this will be where<br>you will introduce<br>some plan or something<br>about your self</p>
      <a class="hero-more" href="#">Read More...</a>
    </div>
  </section>

  <main class="content-panel">
    <h2 class="story-block">Stoyry about how<br>this idea stars</h2>
    <aside class="plans-card">
      <svg width="380" height="477" viewBox="0 0 380 477" aria-hidden="true">
        <polygon points="80,0 380,0 380,477 0,477 0,70" fill="var(--apple-green)"/>
        <polygon points="0,70 80,0 80,70" fill="var(--fold-green)"/>
      </svg>
      <p class="plans-text">introduce your<br>plans or some<br>histories about<br>your clients</p>
    </aside>
  </main>

  <footer class="site-footer">
    <div class="footer-legal">
      <p>Copyright © 2013 Krelto Consulting. Use of this website constitutes acceptance of our User Agreement and Privacy Policy.</p>
      <p class="note">*Conditions apply please see our money back refund policy.</p>
    </div>
  </footer>
</body>
</html>
```